Business Cards for Financial Service Consulting Business Ltd

Business Card Design for my risk management consultancy to the financial service industry
Responsible Lending, Fair Charges, Ethical Collections

Should be serious, professional, corporate

Target Market(s)

Fintech, Financial Services Industry

Industry/Entity Type

Financial Service

Contact Information for Business Card

Lewis Marsh
lew@slatewellconsulting.co.uk
07931520478
01632960417

Font styles to use
Serif

Colors

Designer to choose colors to be used in the design.

Requirements
Must have
• Name: Slatewell Consulting
• Logo, contact details
• The three pillars of my business Responsible Lending, Fair Charges, Ethical Collections
Nice to have
• Corporate Feel
Should not have
• jokes, pretty pictures, cartoons

```html
<!DOCTYPE html>
<html lang="en">
<head>
<meta charset="utf-8">
<title>Slatewell Consulting – Business Cards</title>
<link rel="stylesheet" href="https://fonts.googleapis.com/css2?family=Open+Sans:wght@400;600;700&display=swap">
<style>
  :root {
    --backdrop: #e8e5e1;
    --card-white: #ffffff;
    --brand-green: #79ad47;
    --text-grey: #555555;
    --rule-grey: #5a5a5a;
    --on-green: #ffffff;
  }
  * { box-sizing: border-box; margin: 0; padding: 0; }
  html, body {
    width: 1200px; height: 1000px; overflow: hidden;
    background: var(--backdrop);
    font-family: "Open Sans", Arial, sans-serif;
  }
  .canvas { position: relative; width: 1200px; height: 1000px; }
  .card {
    position: absolute; left: 266px; width: 666px; height: 397px;
    border-radius: 24px; overflow: hidden;
    box-shadow: 0 4px 14px rgba(0,0,0,0.18);
  }
  .card--front { top: 74px; background: var(--card-white); }
  .card--back { top: 533px; background: var(--brand-green); }

  /* front: brand block */
  .brand-front {
    position: absolute; left: 40px; top: 110px; width: 290px;
    display: flex; flex-direction: column; align-items: center;
    color: var(--brand-green);
  }
  .brand-mark-square {
    width: 34px; height: 34px; background: var(--brand-green); margin-bottom: 18px;
  }
  .brand-name {
    font-weight: 600; font-size: 27px; letter-spacing: 1px;
    text-transform: uppercase; text-align: center; line-height: 1.2;
  }

  /* front: contact block */
  .holder-name {
    position: absolute; left: 368px; top: 120px;
    color: var(--brand-green); font-weight: 700; font-size: 22px; letter-spacing: 0.3px;
    text-transform: uppercase;
  }
  .holder-rule {
    position: absolute; left: 370px; right: 0; top: 158px;
    height: 2px; background: var(--rule-grey);
  }
  .contact-list { position: absolute; left: 368px; top: 195px; list-style: none; }
  .contact-item {
    display: flex; align-items: center; gap: 7px;
    color: var(--text-grey); font-size: 16px; line-height: 24px;
  }
  .contact-item--email { margin-top: 8px; }
  .contact-icon { width: 14px; height: 14px; fill: var(--brand-green); flex: none; }

  /* back */
  .brand-back {
    position: absolute; left: 0; right: 0; top: 120px;
    display: flex; flex-direction: column; align-items: center;
    color: var(--on-green);
  }
  .brand-back .brand-mark-square { background: var(--on-green); width: 44px; height: 44px; margin-bottom: 26px; }
  .brand-back .brand-name { font-size: 42px; }
  .pillars {
    position: absolute; left: 0; right: 0; top: 347px; text-align: center;
    color: var(--on-green); font-size: 16px;
  }
</style>
</head>
<body>
<main class="canvas">
  <section class="card card--front">
    <div class="brand-front">
      <div class="brand-mark-square"></div>
      <div class="brand-name">Slatewell Consulting</div>
    </div>
    <h1 class="holder-name">Lewis Marsh</h1>
    <div class="holder-rule"></div>
    <ul class="contact-list">
      <li class="contact-item">
        <svg class="contact-icon" viewBox="0 0 16 16"><path d="M1 6c0-2 3-3.5 7-3.5S15 4 15 6l-3 1.2-1.2-1.8H5.2L4 7.2 1 6zm3 2h8l2 6H2l2-6zm4 1.2a2 2 0 1 0 0 4 2 2 0 0 0 0-4z"/></svg>
        07931520478
      </li>
      <li class="contact-item">
        <svg class="contact-icon" viewBox="0 0 16 16"><path d="M1 6c0-2 3-3.5 7-3.5S15 4 15 6l-3 1.2-1.2-1.8H5.2L4 7.2 1 6zm3 2h8l2 6H2l2-6zm4 1.2a2 2 0 1 0 0 4 2 2 0 0 0 0-4z"/></svg>
        01632960417
      </li>
      <li class="contact-item contact-item--email">
        <svg class="contact-icon" viewBox="0 0 16 16"><path d="M1 3h14v10H1V3zm1.5 1.2L8 8.6l5.5-4.4H2.5z"/></svg>
        lew@slatewellconsulting.co.uk
      </li>
    </ul>
  </section>

  <section class="card card--back">
    <div class="brand-back">
      <div class="brand-mark-square"></div>
      <div class="brand-name">Slatewell Consulting</div>
    </div>
    <p class="pillars">Responsible Lending, Fair Charges, Ethical Collections</p>
  </section>
</main>
</body>
</html>
```